Corvantis websites redesign

Www.cor-vantis.com needs to be redesigned along with updations. The incremental material will be provided for the updations. We are looking for complete redesign of the pages with the new content. The complete write up will be provided soon

Target Market(s)

Global

Coding

Coded - Design and coding required

Number of Pages Required

5+ page

Requirements
Must have
• A clean and slick design for the Consulting.
Should not have
• Too many pictures which reduces the speed of the site

```html
<!DOCTYPE html>
<html lang="en">
<head>
<meta charset="utf-8">
<title>Corvantis — Home</title>
<link href="https://fonts.googleapis.com/css2?family=Open+Sans:wght@400;600;700;800&display=swap" rel="stylesheet">
<style>
:root{
  --ink:#2b2b2b;
  --text:#4a4a4a;
  --navy:#273453;
  --teal:#27d0cf;
  --sky:#2bb7e6;
  --ring:#cfd6de;
  --button:#3aa6cf;
  --accent:#8a1c22;
  --band:#f5f5f5;
  --footer:#131313;
  --white:#ffffff;
}
*{margin:0;padding:0;box-sizing:border-box}
html,body{width:840px;height:1200px;overflow:hidden;background:var(--white)}
body{font-family:"Open Sans",Arial,sans-serif;color:var(--text);position:relative}
h2{font-weight:400}
.site-header{position:absolute;left:0;top:0;width:840px;height:63px}
.brand{position:absolute;left:68px;top:18px;display:flex;align-items:center;gap:8px;font-size:21px;color:var(--navy);font-weight:400}
.brand-dot{width:24px;height:24px;border-radius:50%;background:var(--navy)}
.main-nav{position:absolute;top:27px;left:0;width:840px;font-size:9.5px;letter-spacing:.4px;text-transform:uppercase;color:var(--ink)}
.main-nav a{position:absolute;color:inherit;text-decoration:none;white-space:nowrap}
.main-nav a.current{color:var(--accent)}
.hero{position:absolute;left:0;top:63px;width:840px;height:359px;
  background:radial-gradient(ellipse at 30% 35%,#4f8fd6 0%,#1f4f8f 30%,#11294d 62%,#0a1628 100%)}
.hero-copy{position:absolute;right:68px;top:130px;text-align:right;color:var(--white)}
.hero-title{font-size:22px;font-weight:800;letter-spacing:1px;line-height:26px}
.hero-sub{font-size:15.5px;line-height:22px;letter-spacing:.5px;margin-top:2px}
.slider-arrow{position:absolute;top:229px;width:30px;height:30px}
.slider-arrow.prev{left:22px}
.slider-arrow.next{left:788px}
.trade-title{position:absolute;top:443px;left:0;width:840px;text-align:center;font-size:14px;font-weight:400;letter-spacing:.8px;color:var(--ink)}
.trade-dial{position:absolute;top:475px;width:150px;height:150px}
.about{position:absolute;left:0;top:646px;width:840px;height:213px;background:radial-gradient(ellipse at center,#ffffff 0%,var(--band) 100%)}
.section-title{font-size:14px;letter-spacing:.8px;color:var(--ink);font-weight:400}
.about .section-title{position:absolute;top:31px;width:840px;text-align:center}
.about-text{position:absolute;left:68px;top:61px;width:704px;font-size:9px;letter-spacing:.15px;line-height:12px;text-align:center;hyphens:auto}
.btn{position:absolute;height:23px;width:78px;background:var(--button);color:var(--white);font-size:8.5px;font-weight:600;display:flex;align-items:center;justify-content:center}
.about .btn{left:381px;top:164px}
.founder-photo{position:absolute;left:68px;top:909px;width:244px;height:157px;
  background:linear-gradient(160deg,#3c2f6a 0%,#5a3a5e 45%,#8a3b2e 80%,#b5612c 100%)}
.founder .section-title{position:absolute;left:348px;top:904px}
.founder-name{position:absolute;left:350px;top:924px;font-size:11px;font-weight:600;color:var(--ink);letter-spacing:.3px}
.founder-text{position:absolute;left:348px;top:946px;width:424px;font-size:8.5px;line-height:12px;hyphens:auto}
.founder .btn{left:347px;top:1043px}
.site-footer{position:absolute;left:0;top:1144px;width:840px;height:56px;background:var(--footer)}
.social{position:absolute;left:70px;top:21px;display:flex;gap:14px}
.social span{width:13px;height:13px;border-radius:50%;background:#9a9a9a}
.copyright{position:absolute;right:68px;top:21px;font-size:9.5px;color:#cfcfcf}
</style>
</head>
<body>
<header class="site-header">
  <div class="brand"><span class="brand-dot"></span>Corvantis</div>
  <nav class="main-nav">
    <a class="current" style="left:348px">Home</a>
    <a style="left:403px">Founder</a>
    <a style="left:476px">Consultancy</a>
    <a style="left:572px">System</a>
    <a style="left:635px">Case Studies</a>
    <a style="left:726px">Contact</a>
  </nav>
</header>

<section class="hero" role="img" aria-label="Photo of an open hand holding a glowing dotted world map on a deep blue background">
  <svg class="slider-arrow prev" viewBox="0 0 30 30"><circle cx="15" cy="15" r="15" fill="#5a6470" opacity=".8"/><path d="M17.5 9 L11.5 15 L17.5 21" stroke="#222" stroke-width="2.4" fill="none"/></svg>
  <div class="hero-copy">
    <div class="hero-title">LOREM IPSUM DOLOR SIT</div>
    <div class="hero-sub">amet, consectetur ad<br>ipiscing elit.</div>
  </div>
  <svg class="slider-arrow next" viewBox="0 0 30 30"><circle cx="15" cy="15" r="15" fill="#3b4450" opacity=".85"/><path d="M12.5 9 L18.5 15 L12.5 21" stroke="#111" stroke-width="2.4" fill="none"/></svg>
</section>

<h2 class="trade-title">WORLD MERCHANDISING TRADE 2012 ( USD BILLION)</h2>

<svg class="trade-dial" style="left:76px" viewBox="0 0 150 150">
  <circle cx="75" cy="75" r="52" fill="none" stroke="var(--ring)" stroke-width="3"/>
  <circle cx="75" cy="75" r="56" fill="none" stroke="var(--teal)" stroke-width="3" stroke-dasharray="68 400" transform="rotate(-90 75 75) scale(1 -1) translate(0 -150)"/>
  <circle cx="75" cy="75" r="18" fill="var(--navy)"/>
  <text x="75" y="78.5" text-anchor="middle" font-size="9" fill="#fff" font-family="Open Sans, sans-serif">0-250</text>
</svg>
<svg class="trade-dial" style="left:255px" viewBox="0 0 150 150">
  <circle cx="75" cy="75" r="55" fill="none" stroke="var(--ring)" stroke-width="3"/>
  <circle cx="75" cy="75" r="57" fill="none" stroke="var(--teal)" stroke-width="4" stroke-dasharray="125 400" transform="rotate(-90 75 75) scale(1 -1) translate(0 -150)"/>
  <circle cx="75" cy="75" r="24" fill="var(--navy)"/>
  <text x="75" y="78.5" text-anchor="middle" font-size="9" fill="#aab" font-family="Open Sans, sans-serif">250-500</text>
</svg>
<svg class="trade-dial" style="left:437px" viewBox="0 0 150 150">
  <circle cx="75" cy="75" r="58" fill="none" stroke="var(--teal)" stroke-width="3.5" stroke-dasharray="295 400" transform="rotate(-90 75 75) scale(1 -1) translate(0 -150)"/>
  <circle cx="75" cy="75" r="29" fill="var(--navy)"/>
  <text x="75" y="78.5" text-anchor="middle" font-size="9" fill="#fff" font-family="Open Sans, sans-serif">500-1000</text>
</svg>
<svg class="trade-dial" style="left:616px" viewBox="0 0 150 150">
  <circle cx="75" cy="75" r="58" fill="none" stroke="var(--sky)" stroke-width="4"/>
  <circle cx="75" cy="75" r="52" fill="none" stroke="var(--ring)" stroke-width="3"/>
  <circle cx="75" cy="75" r="28" fill="var(--navy)"/>
  <text x="75" y="78.5" text-anchor="middle" font-size="9" fill="#ccd" font-family="Open Sans, sans-serif">&gt;1000</text>
</svg>

<section class="about">
  <h2 class="section-title">ABOUT US</h2>
  <p class="about-text">Corvantis Consultancy Limited capitalizes on synergies arising from trade and investment linkages between countries and knowledge of traditional and non-traditional pools of liquidity to provide consultancy services to Emerging country banks, Corporates and SMEs. The Consultancy provides bank neutral views to Corporates and SMEs in Asian emerging markets and helps in improving financial structure and efficient use of funds. Our endeavor is to provide a distinct bottom line advantage to our clients. The primary focus is in regionalisation of the banking relationship across the globe, providing structured finance solutions and off balance sheet solutions.The consultancy for the Banks and Non Banking Financial Institutions is focused on risk mitigation techniques, Export Credit Agency business and trade origination and distribution strategies along with raising long term liabilities. e invest actively in developing technology platform for better distribution, disintermediation, efficient process flow and cost effective delivery of solutions.</p>
  <div class="btn">Read More</div>
</section>

<section class="founder">
  <div class="founder-photo" role="img" aria-label="Photo of the founder speaking at a podium during a business conference"></div>
  <h2 class="section-title">FOUNDER</h2>
  <div class="founder-name">Meera Vashani</div>
  <p class="founder-text">Ms. Meera Vashani is the founder director of Corvantis Consultancy Limited (CCL) based at Hong Kong. Meera worked as the Alternate Chief Executive of Halvern Crest Bank, Hong Kong Branch until Jan 2013, heading Corporate Banking business in North Asia and Export Credit Agency business globally. During her tenure, both the businesses increased multifold. Meera started her banking career with Halvern Crest Bank Ltd, India's second largest bank in the year 2002 and in the next 10 years handled multiple leadership responsibilities in the Corporate, Institutional and International Banking space across India, North Asia, Americas and Europe.</p>
  <div class="btn">Read More</div>
</section>

<footer class="site-footer">
  <div class="social" aria-label="Social links"><span></span><span></span><span></span><span></span></div>
  <div class="copyright">© yoursite - All Rights Reserved</div>
</footer>
</body>
</html>
```